Design a CD Cover For Baby Music and Lullabies To Appear on Tunvale Store etc.

Please read this brief before you design. Otherwise you will be wasting your time.

I need a cd cover for music albums which will appear on streaming sites such as Tunvale Store Melodrift, Vimtro etc. for the brand Snug Cradle Tunes. The thumbnails are quite small so the text needs to be quite large.

I need a design if possible, in which I can simply alter the title of the album and the baby picture so that each album has a different cover but works with the branding.

You can check out the Snug Cradle Tunes on the Tunvale store.
https://play.melodriftaudio.net/artist/8kQ3xTnRwLpV27hYbMdZc4

I made those covers and I really don't like them at all! As you can tell I am not a graphic designer. Ha.

Please help me with a modern, eye catching and cute design that will work across the brand now and in the future. The SCT logo and the name Snug Cradle Tunes is the only thing that needs to be used somewhere in the design.

Please use the title

Gentle Static Hums For Nap Time Series A

for this first album.
(White noise sounds are hair dryers, vacuum cleaners, fans, wind, rain, the sea, white noise, pink noise, brown noise etc. )

Here is an example of album covers which are coherent. A style like this without the over the top text would be good. But don't copy these!
https://play.melodriftaudio.net/artist/9TqWmLx5Rb2Hn7KcVpYe1z

Target Market(s)

Parents of babies.

Font styles to use
Serif
Sans Serif

Colors

Designer to choose colors to be used in the design.

Requirements
Must have
• Large font so it can been seen in the melodrift thumbnail. A photo of a baby. Please take a look at the melodrift and tunvale stores. The Snug Cradle Tunes logo.
• Album Title
• Gentle Static Hums For Nap Time Series A

```html
<!DOCTYPE html>
<html lang="en">
<head>
<meta charset="utf-8">
<title>Gentle Static Hums For Nap Time – Series A</title>
<link href="https://fonts.googleapis.com/css2?family=Montserrat:wght@600;700;800&display=swap" rel="stylesheet">
<style>
  :root {
    --stage-top: #6fadb4;
    --stage-mid: #3e5f63;
    --stage-bottom: #121314;
    --cover-paper: #fbf4f4;
    --skin: #e9a597;
    --skin-deep: #c97a6e;
    --blanket: #f4ecec;
    --stripe-blue: #9fb8cc;
    --stripe-pink: #d9a6b4;
    --ink-teal: #2f5a62;
    --ink-coral: #f07f68;
    --ink-rust: #8e2f1d;
    --ink-dark: #2a1a18;
    --brand-blue: #1b6fb8;
    --caption: #ffffff;
  }
  * { margin: 0; padding: 0; box-sizing: border-box; }
  html, body { width: 1200px; height: 1200px; overflow: hidden; }
  body {
    background: linear-gradient(180deg, var(--stage-top) 0%, var(--stage-mid) 45%, var(--stage-bottom) 100%);
    font-family: "Montserrat", sans-serif;
    position: relative;
  }
  .album-cover {
    position: absolute;
    left: 181px; top: 131px;
    width: 847px; height: 847px;
    background: var(--cover-paper);
    overflow: hidden;
    box-shadow: 0 10px 30px rgba(0,0,0,0.18);
  }
  .baby-photo {
    position: absolute;
    left: 0; top: 0; width: 100%; height: 640px;
    background:
      radial-gradient(ellipse 28% 40% at 50% 42%, var(--skin) 0%, var(--skin-deep) 55%, rgba(233,165,151,0) 100%),
      radial-gradient(ellipse 60% 25% at 50% 82%, var(--blanket) 0%, rgba(244,236,236,0) 100%),
      repeating-linear-gradient(180deg, var(--stripe-blue) 0 14px, #f3eef0 14px 30px, var(--stripe-pink) 30px 44px, #f3eef0 44px 60px);
    -webkit-mask-image: radial-gradient(ellipse 62% 62% at 50% 42%, #000 55%, transparent 100%);
            mask-image: radial-gradient(ellipse 62% 62% at 50% 42%, #000 55%, transparent 100%);
    opacity: 0.9;
  }
  .brand-mark {
    position: absolute;
    right: 50px; top: 60px;
    display: flex; align-items: center; gap: 10px;
    font-weight: 700; font-size: 18px;
    color: var(--brand-blue);
  }
  .brand-mark .dot {
    width: 26px; height: 26px; border-radius: 50%;
    background: var(--brand-blue);
  }
  .cover-title {
    position: absolute;
    left: 0; right: 0; top: 583px;
    text-align: center;
  }
  .title-main, .title-sub {
    font-weight: 800;
    background: linear-gradient(90deg, var(--ink-teal) 0%, var(--ink-rust) 35%, var(--ink-teal) 55%, var(--ink-coral) 78%, var(--ink-coral) 100%);
    -webkit-background-clip: text; background-clip: text;
    color: transparent;
  }
  .title-main {
    font-size: 56px; line-height: 1; letter-spacing: 3px;
  }
  .title-sub {
    margin-top: 18px;
    font-size: 42px; line-height: 1; letter-spacing: 5px;
  }
  .title-series {
    margin-top: 50px;
    font-weight: 700; font-size: 26px; letter-spacing: 20px;
    padding-left: 20px;
    background: linear-gradient(90deg, var(--ink-coral), var(--ink-rust) 50%, var(--ink-dark));
    -webkit-background-clip: text; background-clip: text;
    color: transparent;
  }
  .album-caption {
    position: absolute;
    left: 0; right: 0; top: 1008px;
    text-align: center;
    color: var(--caption);
    font-weight: 700; font-size: 48px; line-height: 60px; letter-spacing: 3px;
  }
</style>
</head>
<body>
  <section class="album-cover">
    <div class="baby-photo" role="img" aria-label="Photo of a newborn baby swaddled in a white blanket on a striped hospital blanket"></div>
    <div class="brand-mark"><span class="brand-name">Snug Cradle Tunes</span><span class="dot"></span></div>
    <div class="cover-title">
      <h1 class="title-main">GENTLE STATIC HUMS</h1>
      <h2 class="title-sub">FOR NAP TIME</h2>
      <p class="title-series">SERIES A</p>
    </div>
  </section>
  <p class="album-caption">Gentle Static Hums<br>for Nap Time</p>
</body>
</html>
```